Postcard Design

Hoofmere Ftness Center is a state of the art equine rehabilitation and fitness center. We offer a wide variety of options to get your equine partner in tip top performing condition. Whether is swimming in or 11 foot deep pool or exercising in the squatted, we provide a personalized program for your special horse. Some other services offered are StallAir breathing treatments, pulso drift and gallotone.
Updates
Project Deadline Extended Reason: Since the project was started we have opened for business and I have pictures using my equipment at our place of business that I would like to add to the project to be used. I have also received my logo design from one of your designers that I would like added to this project. Added Tuesday, March 15, 2016
Industry/Entity Type
Fitness
Look and feel
Each slider illustrates characteristics of the customer's brand and the style your logo design should communicate.

```html
<!DOCTYPE html>
<html lang="en">
<head>
<meta charset="utf-8">
<title>Hoofmere Ftness Center Postcard</title>
<link href="https://fonts.googleapis.com/css2?family=Jost:wght@400;500;600;700&display=swap" rel="stylesheet">
<style>
:root{
  --backdrop:#d6d4d5;
  --purple:#5703bf;
  --purple-deep:#4a02a6;
  --yellow:#fdc732;
  --cyan:#17d8ee;
  --white:#ffffff;
  --ink:#1a1a1a;
  --stamp:#e4e4e6;
  --rule:#7a7a7a;
}
*{margin:0;padding:0;box-sizing:border-box}
html,body{width:900px;height:1200px;overflow:hidden}
body{background:var(--backdrop);font-family:"Jost",sans-serif;position:relative}
.card{position:absolute;left:132px;width:636px;overflow:hidden;box-shadow:3px 4px 6px rgba(0,0,0,.35)}
.card--front{top:80px;height:491px}
.card--back{top:614px;height:489px;background:var(--white)}
.fill{position:absolute}
.shapes{position:absolute;left:0;top:0}

/* front */
.front-photo{left:0;top:0;width:636px;height:491px;
  background:linear-gradient(160deg,#5a4a3c 0%,#7b8d86 28%,#3fa3a6 55%,#2c6f78 78%,#5fb9bd 100%)}
.front-art{right:0;top:0;width:192px;height:142px;
  background:radial-gradient(circle at 55% 50%,#e23b8a 0%,#3db8e8 30%,#f2c230 48%,#101010 72%)}
.service{position:absolute;background:var(--yellow);color:var(--ink);font-size:17px;font-weight:500;
  height:28px;line-height:28px;border-radius:4px;padding:0 16px}
.service--first{left:136px;top:322px;width:288px}
.service--second{left:204px;top:359px;width:220px;text-align:right;padding-right:26px}
.service--third{left:204px;top:395px;width:220px;text-align:right;padding-right:26px}
.offer{position:absolute;left:417px;top:303px;width:170px;text-align:center;color:var(--white)}
.offer__title{font-size:31px;font-weight:700;color:var(--yellow);line-height:1.05}
.offer__text{font-size:14px;line-height:17.5px;margin-top:3px}
.front-url{position:absolute;right:26px;top:454px;color:var(--white);font-size:15.5px}

/* back */
.back-photo{left:0;top:0;width:460px;height:230px;
  background:linear-gradient(180deg,#1c1a16 0%,#5a3a22 40%,#8a5a36 70%,#4a5a4a 100%);
  clip-path:polygon(0 0,448px 0,374px 216px,0 216px)}
.tagline{position:absolute;left:0;top:218px;width:390px;height:28px;background:var(--cyan);
  color:var(--ink);font-size:13.5px;line-height:28px;padding-left:10px}
.back-info{position:absolute;left:18px;top:258px;color:var(--white)}
.heading{font-size:18px;font-weight:500;color:var(--yellow);display:inline-block;
  border-bottom:1px solid var(--yellow);padding-right:6px;line-height:1.2}
.about{font-size:15.5px;line-height:20px;margin-top:6px;width:340px}
.heading--contact{margin-top:14px}
.contact{list-style:none;margin-top:8px;font-size:15.5px;line-height:20px}
.contact li{display:flex;align-items:center;gap:10px}
.contact svg{width:13px;height:13px;flex:none}
.stamp{position:absolute;left:539px;top:27px;width:66px;height:65px;background:var(--stamp)}
.address-line{position:absolute;left:388px;width:216px;height:1px;background:var(--rule)}
</style>
</head>
<body>

<section class="card card--front">
  <div class="fill front-photo" role="img" aria-label="Photo of a dark horse being led through a therapy swimming pool"></div>
  <div class="fill front-art" role="img" aria-label="Colourful line illustration of a horse head on black"></div>
  <svg class="shapes" width="636" height="491" viewBox="0 0 636 491">
    <path d="M0 466 Q380 460 636 292 L636 491 L0 491 Z" fill="var(--purple)"/>
    <path d="M0 459 Q380 453 636 285" fill="none" stroke="var(--cyan)" stroke-width="6"/>
    <circle cx="502" cy="360" r="86" fill="var(--purple)"/>
  </svg>
  <div class="service service--first">StallAir breathing treatments</div>
  <div class="service service--second">Pulso drift</div>
  <div class="service service--third">Gallotone</div>
  <div class="offer">
    <div class="offer__title">We offer</div>
    <div class="offer__text">a wide variety of<br>options to get your<br>equine partner in<br>tip top performing<br>condition</div>
  </div>
  <div class="front-url">www.website.com</div>
</section>

<section class="card card--back">
  <svg class="shapes" width="636" height="489" viewBox="0 0 636 489">
    <polygon points="0 216 374 216 281 489 0 489" fill="var(--purple)"/>
  </svg>
  <div class="fill back-photo" role="img" aria-label="Photo of three horses looking over a stable door"></div>
  <div class="tagline">We provide a personalized program for your special horse</div>
  <div class="back-info">
    <h2 class="heading">About Us:</h2>
    <p class="about">Hoofmere Ftness Center is a state of the<br>art equine rehabilitation and fitness center.</p>
    <h2 class="heading heading--contact">Contact Us:</h2>
    <ul class="contact">
      <li><svg viewBox="0 0 16 16"><path d="M3 1.5l3 3-1.6 1.8a9 9 0 0 0 5.3 5.3L11.5 10l3 3-1.8 1.8C7 15 1 9 1.2 3.3Z" fill="var(--white)"/></svg>0123-456-789</li>
      <li><svg viewBox="0 0 16 16"><rect x="1" y="3" width="14" height="10" fill="var(--white)"/><path d="M1 3l7 6 7-6" fill="none" stroke="var(--purple)" stroke-width="1.4"/></svg>info@mail.com</li>
      <li><svg viewBox="0 0 16 16"><circle cx="8" cy="8" r="6.5" fill="none" stroke="var(--white)" stroke-width="1.4"/><path d="M1.5 8h13M8 1.5c-3 3.5-3 9.5 0 13M8 1.5c3 3.5 3 9.5 0 13" fill="none" stroke="var(--white)" stroke-width="1.2"/></svg>www.website.com</li>
    </ul>
  </div>
  <div class="stamp"></div>
  <div class="address-line" style="top:294px"></div>
  <div class="address-line" style="top:326px"></div>
  <div class="address-line" style="top:358px"></div>
</section>

</body>
</html>
```